Independent Midwife for a positive birth experience needs a vibrant, and elegant business card/logo

I need a business card design with a logo. The logo I would like to be able to use on my website (www.midwifemarisol.com) next to my name.
Therefore the design of the card and logo should suit the colours and design of the website. The title of the website and company is "Marisol Quenby Fairhurst, Midwife" but I'd like to have the business card title to be "Marisol Quenby Fairhurst - Independent Midwife" in bold letters, same script font as in my website.

I provide gold standard midwifery services, one-to-one tailored care, continuity of care throughout the entire pregnancy (antenatal care), the birth and after the birth (postnatal care), home birth, water birth, breast-feeding support, and birth preparation workshops. I also am certified and offer complementary therapies: pregnancy reflexology, rebozo techniques for optimal baby positioning.

The design should incorporate similar colours and style as the website and the "Marisol Quenby Fairhurst - Independent Midwife" on the card should include the same font as in the title of the website, however, in bold. The front of the card should have a logo, title and contact information (phone number 072639518, email marisol.fairhurst@lovantamail.com, website address www.midwifemarisol.com).
The back of the card to include the services I offer.

The logo: use of colour purple (varying shades), should communicate communicate warmth, kindness, compassion. It should convey that I'm a midwife who believes in fostering a trusting relationship with my clients and to provide them with a positive pregnancy and birth experience.

Target Market(s)

Pregnant women or women who are looking to book a private midwife for better birth experience and outcome

Industry/Entity Type

Baby

Contact Information for Business Card

Name and Title on front side together with contact details
The reverse side should have services/packages offered

Font styles to use
Script
Other font styles liked:
• similar script as in my website for name and title, and easy to read font for the rest of the words

Colors
b768aa
a54599
d2a4cc
ffffff

Requirements
Must have
• same font as title of website, but slightly bolder.
• similar design, colours, patterns as in website.
• Also include a gold accent colour somewhere in the design please.
Nice to have
• perhaps a logo of pregnant belly in profile or newborn baby icon

```html
<!DOCTYPE html>
<html lang="en">
<head>
<meta charset="utf-8">
<title>Marisol Quenby Fairhurst - Independent Midwife</title>
<link rel="stylesheet" href="https://fonts.googleapis.com/css2?family=Dancing+Script:wght@600&family=Quicksand:wght@400;500;700&display=swap">
<style>
  :root {
    --plum: #a54599;
    --orchid: #b768aa;
    --lilac: #d2a4cc;
    --lilac-soft: #e3c6df;
    --mist: #eadcec;
    --paper: #f7f6f5;
    --gold-light: #f3c94a;
    --gold-deep: #c48a12;
  }
  * { margin: 0; padding: 0; box-sizing: border-box; }
  html, body {
    width: 1200px;
    height: 758px;
    overflow: hidden;
    background: var(--paper);
  }
  .business-card {
    position: relative;
    width: 1200px;
    height: 758px;
    background: var(--paper);
    overflow: hidden;
  }
  .card-shapes {
    position: absolute;
    inset: 0;
  }
  .brand-mark {
    position: absolute;
    left: 40px;
    top: 190px;
    width: 300px;
    display: flex;
    flex-direction: column;
    align-items: center;
    gap: 18px;
  }
  .brand-dot {
    width: 110px;
    height: 110px;
    border-radius: 50%;
    border: 6px solid var(--mist);
  }
  .brand-name {
    font-family: "Quicksand", sans-serif;
    font-weight: 500;
    font-size: 34px;
    line-height: 1.15;
    color: var(--mist);
    text-align: center;
  }
  .gold-accent {
    position: absolute;
    left: 205px;
    top: 575px;
    width: 110px;
    height: 62px;
    border-radius: 60% 40% 55% 45%;
    background: linear-gradient(135deg, var(--gold-light), var(--gold-deep));
  }
  .identity {
    position: absolute;
    left: 420px;
    top: 118px;
  }
  .identity-name {
    font-family: "Dancing Script", cursive;
    font-weight: 600;
    font-size: 62px;
    color: var(--plum);
    line-height: 1.1;
  }
  .identity-title {
    font-family: "Quicksand", sans-serif;
    font-weight: 500;
    font-size: 34px;
    color: var(--orchid);
    margin-top: 14px;
  }
  .contact {
    position: absolute;
    left: 585px;
    top: 528px;
    font-family: "Quicksand", sans-serif;
    color: var(--orchid);
    list-style: none;
  }
  .contact li {
    font-size: 30px;
    font-weight: 500;
    line-height: 1.35;
    letter-spacing: 0.5px;
  }
  .contact .contact-web {
    font-weight: 700;
    color: var(--plum);
    font-size: 32px;
    margin-top: 6px;
  }
</style>
</head>
<body>
  <main class="business-card">
    <svg class="card-shapes" width="1200" height="758" viewBox="0 0 1200 758" aria-hidden="true">
      <polygon class="top-band" points="360,0 1200,0 1200,90 380,90" fill="#dcb6d8"/>
      <polygon class="side-panel" points="0,0 360,0 530,758 0,758" fill="#a54599"/>
    </svg>

    <div class="brand-mark">
      <span class="brand-dot"></span>
      <span class="brand-name">Marisol<br>Fairhurst</span>
    </div>

    <div class="gold-accent" role="img" aria-label="Gold leaf flourish ornament"></div>

    <header class="identity">
      <h1 class="identity-name">Marisol Quenby Fairhurst</h1>
      <p class="identity-title">Independent Midwife</p>
    </header>

    <ul class="contact">
      <li class="contact-phone">072639518</li>
      <li class="contact-email">marisol.fairhurst@lovantamail.com</li>
      <li class="contact-web">www.midwifemarisol.com</li>
    </ul>
  </main>
</body>
</html>
```